Brisk Venture - Logo & Business Card

I have briefly designed a logo for my small events business and need it fixed up. I would prefer it to be white on black background. I also need a PDF for business cards, I would like them to be black with the logo on one side and my details on the other side:

Brisk Venture
Corinna-May Feltwell
Founder / Director
0471 820 237
corinna@briskventure.com.au

```html
<!DOCTYPE html>
<html lang="en">
<head>
<meta charset="utf-8">
<title>Brisk Venture – Business Cards</title>
<link href="https://fonts.googleapis.com/css2?family=Didact+Gothic&family=Montserrat:wght@600&display=swap" rel="stylesheet">
<style>
  :root {
    --backdrop: #f1f1f1;
    --card: #000000;
    --ink: #ffffff;
    --accent: #22d3c5;
    --muted: #e6e6e6;
  }
  * { margin: 0; padding: 0; box-sizing: border-box; }
  html, body {
    width: 1200px;
    height: 1000px;
    overflow: hidden;
    background: radial-gradient(circle at 50% 45%, #ffffff 0%, var(--backdrop) 70%);
    font-family: "Didact Gothic", "Century Gothic", sans-serif;
  }
  .stage {
    position: relative;
    width: 1200px;
    height: 1000px;
  }
  .card {
    position: absolute;
    top: 355px;
    width: 500px;
    height: 290px;
    background: var(--card);
    box-shadow: 0 6px 18px rgba(0,0,0,0.18);
  }
  .card--details { left: 80px; }
  .card--brand { left: 620px; }

  /* Details side */
  .wordmark {
    position: absolute;
    display: flex;
    align-items: center;
    gap: 10px;
    color: var(--accent);
    font-family: "Didact Gothic", sans-serif;
    white-space: nowrap;
  }
  .wordmark__dot {
    border-radius: 50%;
    background: var(--accent);
    flex: none;
  }
  .card--details .wordmark {
    left: 42px;
    top: 108px;
    font-size: 25px;
  }
  .card--details .wordmark__dot { width: 14px; height: 14px; }

  .divider {
    position: absolute;
    left: 232px;
    top: 22px;
    width: 2px;
    height: 150px;
    background: var(--accent);
  }
  .contact {
    position: absolute;
    left: 256px;
    top: 48px;
    color: var(--ink);
  }
  .contact__name {
    font-family: "Montserrat", sans-serif;
    font-weight: 600;
    font-size: 15px;
    letter-spacing: 0.2px;
  }
  .contact__role {
    margin-top: 4px;
    font-size: 13px;
    letter-spacing: 2.4px;
    color: var(--muted);
  }
  .contact__phone {
    margin-top: 4px;
    font-size: 16px;
    letter-spacing: 4.5px;
  }
  .email {
    position: absolute;
    left: 0;
    right: 0;
    bottom: 40px;
    text-align: center;
    color: var(--ink);
    font-size: 19px;
    letter-spacing: 0.3px;
  }

  /* Brand side */
  .card--brand .wordmark {
    right: 40px;
    bottom: 70px;
    font-size: 44px;
  }
  .card--brand .wordmark__dot { width: 24px; height: 24px; }
</style>
</head>
<body>
  <main class="stage">
    <section class="card card--details" aria-label="Business card, details side">
      <div class="wordmark">
        <span class="wordmark__dot"></span>
        <span class="wordmark__name">Brisk Venture</span>
      </div>
      <div class="divider"></div>
      <div class="contact">
        <p class="contact__name">Corinna-May Feltwell</p>
        <p class="contact__role">FOUNDER / DIRECTOR</p>
        <p class="contact__phone">0471 820 237</p>
      </div>
      <p class="email">corinna@briskventure.com.au</p>
    </section>

    <section class="card card--brand" aria-label="Business card, logo side">
      <div class="wordmark">
        <span class="wordmark__dot"></span>
        <span class="wordmark__name">Brisk Venture</span>
      </div>
    </section>
  </main>
</body>
</html>
```